Designing a new homepage for www.Brindlework.net

WEBSITE: www.brindlework.net

ABOUT THE WEBSITE
The Brindlework.net (BWK) website contains a large directory of over 50,000 international trade service providers that is not valued enough on the homepage (HP). Currently from the HP, the site appears as a general site about imports and exports (international trade). As a result, it contradicts the purpose and experience of the site.
The website is new and original for international trade online: it is a tool to find the best experts and professionals that can help importers and exporters to implement their overseas operations.

Specifically:
a) An exporter who wants to sell in Italy can find on BWK: agents to distribute their products, a lawyer for reviewing contracts, translators to translate brochures and websites, an export consultant, etc. Various local providers that can help sell their products in Italy, a local provider (e.g. based in Italy) are generally more efficient and less costly than a supplier in the exporter’s home country

b) An importer who wants to buy in China will find purchasing agents who source products for third parties; logistics companies that store and ship merchandise; corporate quality control to ensure product quality before shipment, etc.; various local providers based in China to better organize its import operation.

BWK is therefore a very resourceful solution for SMEs who want to develop, improve and organize their international trade:
a) it significantly increases their ability to create new opportunities by using the services of a third party: export to a new country; import a new product
b) it allows them to optimize their purchases of services by seeking alternatives: find a less expensive carrier, a foreign lawyer challenged by a local lawyer

It is the perfect complement to cross border marketplaces (e.g. Quorvanta.com, fenwickmarts.com, zl48.com) which concentrate on the search for products (and of companies/counterparts) but:
a) help the user to import only, not really export
b) do not help implement the operations of exporting/importing from A to Z

Therefore, BWK offers a new way of “easy exporting” (or easy importing).

THE BRIEF

The objective of the project is to rethink the HP (and the site design) to highlight this experience: "export and import more successfully through 50,000+ service providers in over 100 countries”.
We have created a wireframe (see attached) of the structure we feel best meets this objective. What do you think? Do we meet it through our wireframe? Then, next step is to take this wireframe and create a clear design that really helps us to achieve our objective.

It is considered that the site captures the importers/exporters seeking to increase their exports or to better organize their imports (but we do not start from a priori that these users are looking for service providers).
The HP should highlight the importance of service providers addressing export markets or better organizing their imports; the "market analyses" of the site should act as a "knowledge resource", where the site offers more the main experience: if you want to export to a country you have any interest to first explore what the partners listed by BWK can provide.

Reason: We feel that we're seeing some interesting designs and would like to give current and even potential submissions more time. So far we have not seen the one that really strikes us, so perhaps more time is what we and the designers need! Thanks!

Target Market(s)

Importers, exporters, international trade service providers, foreign investors, etc

Industry/Entity Type

Lawyer

Requirements
Must have
• • Please use the current basic design elements of the website, including the logo, (www.brindlework.net). These include colors and fonts, etc. We only aim to change the HP and therefore, only implement a change to the header and footer of the whole site.
• Please find inspiration from our wireframes (attached), as they have been carefully thought about by our own team. However, should you feel the need to challenge the wireframes, please do so in your design, we're interested to see what you can present us.
• Our prime objective in terms of design: creating a more user-friendly interface on the HP to guide users into the rest of the website
• We already have a psd file based on the wireframes we’ve attached to the brief. If you would like this, so your job is easier (such as using same text as we have in the wireframes), let us know!

```html
<!DOCTYPE html>
<html lang="en">
<head>
<meta charset="utf-8">
<title>Brindlework.net – International Trade Service Providers</title>
<link href="https://fonts.googleapis.com/css2?family=Open+Sans:ital,wght@0,300;0,400;0,600;0,700;1,400&family=PT+Serif:wght@400;700&display=swap" rel="stylesheet">
<style>
:root{
  --page:#f2f2f2;
  --white:#ffffff;
  --ink:#444444;
  --muted:#777777;
  --light:#9a9a9a;
  --rule:#d6d6d6;
  --blue:#2f6ea5;
  --blue-dark:#244a6b;
  --blue-band:#35658e;
  --blue-band-2:#2a5578;
  --navy:#203f5b;
  --panel:#e7e7e7;
  --star:#e8a317;
  --red:#c8352b;
}
*{box-sizing:border-box;margin:0;padding:0}
html,body{width:1200px;height:2462px;overflow:hidden}
body{position:relative;background:var(--page);font-family:"Open Sans",Arial,sans-serif;color:var(--ink);font-size:13px}
a{color:var(--blue);text-decoration:none}
ul{list-style:none}
.abs{position:absolute}

/* top bar */
.topbar{left:0;top:0;width:1200px;height:45px;background:linear-gradient(#f4f4f4,#e4e4e4);border-bottom:1px solid #d4d4d4}
.topbar .links{position:absolute;left:128px;top:15px;display:flex;gap:18px;font-size:12px;color:var(--muted)}
.topbar .links .on{color:var(--blue);text-decoration:underline}
.topbar .like{display:flex;align-items:center;gap:4px}
.topbar .like i{display:inline-block;width:11px;height:11px;background:#8a8a8a}
.topbar .acts{position:absolute;right:120px;top:8px;display:flex;gap:8px}
.btn-light{display:inline-block;height:29px;line-height:27px;padding:0 18px;border:1px solid #c6c6c6;border-radius:3px;background:linear-gradient(#fbfbfb,#e6e6e6);font-size:12px;color:#555}

/* header */
.header{left:0;top:46px;width:1200px;height:90px;background:var(--white);border-bottom:1px solid #dadada}
.logo{position:absolute;left:119px;top:30px;display:flex;align-items:center;gap:8px;font-size:24px;letter-spacing:3px;color:var(--blue-dark);font-weight:400}
.logo i{width:16px;height:16px;border-radius:50%;background:var(--blue)}
.nav{position:absolute;left:533px;top:24px;display:flex;align-items:center;gap:32px;font-family:"PT Serif",Georgia,serif;font-size:15px;text-transform:uppercase;color:var(--blue)}
.nav .cur{background:linear-gradient(#2f5676,#1d3a55);color:#fff;padding:0 18px;height:50px;line-height:50px;border-radius:3px;margin-left:2px;box-shadow:0 2px 3px rgba(0,0,0,.3)}

/* hero */
.hero{left:70px;top:148px;width:1060px;height:300px;background:linear-gradient(90deg,#a9a9a9 0%,#cfcfcf 45%,#e9e9e9 100%);box-shadow:0 6px 10px rgba(0,0,0,.15)}
.hero h1{position:absolute;left:46px;top:36px;font-weight:300;font-size:38px;color:#24527d}
.hero .lead{position:absolute;left:50px;top:102px;font-size:15px;font-weight:700;color:#fff}
.hero ul{position:absolute;left:50px;top:130px;color:#fff;font-size:13.5px;line-height:20px}
.hero ul li:before{content:"• "}
.search{position:absolute;left:40px;top:220px;width:496px;height:52px;background:#2e2e2e;border-radius:3px;padding:7px 12px;display:flex}
.search .field{flex:1;background:#fff;height:38px;line-height:38px;padding-left:12px;font-size:13px;color:#888;border-radius:2px 0 0 2px}
.search .go{width:48px;height:38px;background:linear-gradient(#3e7bb0,#275a85);display:flex;align-items:center;justify-content:center}
.hero .photo{position:absolute;left:606px;top:0;width:390px;height:300px;background:radial-gradient(ellipse at 50% 60%,#4c5866 0%,#7d8791 40%,rgba(200,200,200,0) 72%)}
.listed{position:absolute;left:832px;top:221px;width:176px;height:52px;background:#fff;display:flex;align-items:center;gap:10px;padding:0 10px;font-size:10px;color:#666;line-height:12px;box-shadow:0 1px 2px rgba(0,0,0,.2)}
.listed i{width:30px;height:30px;background:#bbb;flex:none;margin-left:auto}

/* start bar */
.start{left:70px;top:498px;width:1060px;height:92px;background:linear-gradient(#3d6f99,var(--blue-band-2));box-shadow:0 4px 8px rgba(0,0,0,.2);display:flex;align-items:center;padding-left:42px;color:#fff}
.start .label{font-size:28px;font-weight:300;margin-right:30px}
.select{width:248px;height:40px;background:#fff;border-radius:3px;display:flex;align-items:center;justify-content:space-between;padding-left:14px;font-size:12.5px;color:#666}
.select b{width:36px;height:40px;border-left:1px solid #ccc;display:flex;align-items:center;justify-content:center}
.start .assist{margin:0 25px 0 22px;font-size:14px}
.chk{display:flex;align-items:center;gap:10px;font-size:14px;margin-right:34px;color:#cfe0ef}
.chk i{width:17px;height:17px;background:#1f3f5c;border:1px solid #173349;display:flex;align-items:center;justify-content:center;font-style:normal;color:#fff;font-size:13px}
.chk.on{color:#fff}
.chk.on i{background:#fff;color:#222}
.gobtn{margin-left:6px;width:72px;height:60px;background:linear-gradient(#4a4a4a,#222);border-radius:3px;display:flex;align-items:center;justify-content:center;font-size:24px;font-weight:600}

/* country panel */
.country{left:70px;top:619px;width:1060px;height:268px;background:var(--panel);border-bottom:3px solid #cfcfcf}
.country h2{position:absolute;left:49px;top:28px;font-weight:400;font-size:27px;color:#3d5874}
.country h2 span{font-size:15px;color:#444;margin-left:8px}
.country .arrows{position:absolute;right:70px;top:34px;display:flex;gap:18px}
.country .rule{position:absolute;left:49px;right:49px;top:82px;border-top:1px solid #cfcfcf}
.seal{position:absolute;left:49px;top:104px;width:58px;height:58px;border-radius:50%;background:#d0d0d0;border:2px solid #bdbdbd}
.partner{position:absolute;left:131px;top:98px;width:340px}
.partner h3{font-size:17px;font-weight:600;color:#3a3a3a}
.partner .sub{font-size:13px;color:#666;margin-bottom:12px}
.partner p{font-size:12px;line-height:17px;color:#777}
.partner .foot{display:flex;justify-content:space-between;margin-top:14px;font-size:12px}
.partner .foot a{text-decoration:underline}
.country .vline{position:absolute;left:477px;top:100px;height:130px;border-left:1px solid #cfcfcf}
.stat{position:absolute;top:104px;width:140px}
.stat .n{font-size:40px;font-weight:300;color:var(--blue);line-height:44px}
.stat .t{font-size:16px;font-weight:600;color:#444;line-height:20px;margin-top:4px}
.stat .w{font-size:12px;color:#777}
.stat a{display:inline-block;margin-top:10px;font-size:12px;color:#555;text-decoration:underline}

/* columns */
.col h4{font-size:16px;font-weight:400;color:var(--blue-dark);padding-bottom:10px;border-bottom:1px solid var(--rule);margin-bottom:18px}
.dir{left:119px;top:922px;width:302px}
.tabs{display:flex;margin-bottom:14px}
.tabs span{flex:1;height:38px;line-height:38px;text-align:center;font-size:13px;background:#e2e2e2;color:#666;border:1px solid #d0d0d0}
.tabs .on{background:linear-gradient(#35658e,#254d70);color:#fff;border-color:#254d70}
.dir ul li{font-size:12.5px;line-height:25.5px;color:#555}
.dir ul li:before{content:"•";color:#999;margin-right:6px}
.dir ul li em{font-style:normal;color:#999}
.dir ul li.sub{padding-left:16px;color:var(--blue);font-weight:700;text-decoration:underline}

.say{left:449px;top:922px;width:300px}
.quote{position:relative;margin-bottom:28px}
.quote .head{display:flex;gap:12px;margin-bottom:10px}
.avatar{width:60px;height:60px;background:linear-gradient(#c9ced4,#7b8590);flex:none}
.quote .nm{font-size:14px;color:var(--blue)}
.quote .role{font-size:16px;color:#333;line-height:19px}
.quote .loc{font-size:11.5px;color:#666}
.quote p{position:relative;z-index:1;font-size:12px;font-style:italic;line-height:17.5px;color:#555}
.quote .mark{position:absolute;z-index:0;right:4px;top:62px;font-size:90px;color:#e9e9e9;font-family:"PT Serif",serif;line-height:1}
.quote .bottom{display:flex;justify-content:space-between;align-items:center;margin-top:14px;font-size:12px;border-top:1px solid var(--rule);padding-top:10px}
.quote .bottom a{text-decoration:underline}
.btn-white{display:inline-block;padding:5px 12px;background:#fff;border:1px solid #d2d2d2;border-radius:2px;font-size:11.5px;color:#333;font-weight:600}

.tips{left:449px;top:1537px;width:300px}
.tip{border-bottom:1px solid var(--rule);padding-bottom:12px;margin-bottom:20px}
.tip h5{font-size:14px;font-weight:400;color:#333;margin-bottom:5px}
.tip p{font-size:12px;color:#777;line-height:16px}
.tip .rate{display:flex;justify-content:flex-end;align-items:center;gap:6px;font-size:11px;color:#666;margin-top:4px}
.stars{color:var(--star);letter-spacing:1px;font-size:12px}
.stars b{color:#c8c8c8;font-weight:400}
.pdf{width:14px;height:16px;background:var(--red);border-radius:1px}
.tips .bottom{display:flex;justify-content:space-between;align-items:center;font-size:11.5px;color:#555;margin-top:-6px}

.newsp{left:778px;top:922px;width:300px}
.prov{display:flex;gap:12px;border-bottom:1px solid var(--rule);padding-bottom:12px;margin-bottom:18px}
.prov .lg{width:84px;flex:none;padding-top:8px;display:flex;align-items:flex-start;gap:5px;font-size:10.5px;font-weight:700;color:#333;line-height:12px;white-space:nowrap}
.prov .lg i{width:9px;height:9px;background:#333;flex:none;margin-top:1px}
.prov h5{font-size:15px;font-weight:400;color:var(--blue);line-height:18px;white-space:nowrap}
.prov .cat{font-size:11.5px;font-weight:600;color:#444;margin-bottom:4px}
.prov p{font-size:11.5px;line-height:15px;color:#666}
.prov a{display:inline-block;margin-top:6px;font-size:11.5px;color:#666}
.free{width:306px;height:112px;background:linear-gradient(#3a6c96,#284f72);color:#fff;padding:16px 18px;box-shadow:0 3px 6px rgba(0,0,0,.2)}
.free .t{font-size:18px;line-height:23px}
.free .t b{font-weight:700}
.free .t .site{font-weight:700;font-size:18px}
.free .b{display:flex;justify-content:space-between;align-items:center;margin-top:8px;font-size:11.5px}
.free .btn-white{color:var(--blue-dark)}

.know{left:778px;top:1537px;width:300px}
.know .intro{font-size:13px;color:#333;margin-bottom:8px}
.know ul li{display:flex;font-size:13px;line-height:21px;color:#444}
.know ul li b{width:55px;color:var(--blue);font-weight:600}
.know ul li:before{content:"•";color:var(--blue);margin-right:6px}
.know .pick{display:flex;gap:10px;margin:18px 0 22px}
.know .pick .select{width:238px;height:38px;border:1px solid #ccc}
.btn-blue{width:56px;height:38px;background:linear-gradient(#3a6c96,#284f72);color:#fff;font-weight:600;display:flex;align-items:center;justify-content:center;border-radius:3px}
.know .pop{font-size:13px;font-weight:600;color:#333;margin-bottom:4px}
.know .countries{font-size:12.5px;line-height:21px;color:#555}
.know .countries u{color:var(--blue)}

/* partners strip */
.partners{left:0;top:2035px;width:1200px;height:110px;background:#fafafa;border-top:1px solid #dcdcdc;border-bottom:1px solid #dcdcdc;display:flex;align-items:center;justify-content:center;gap:46px}
.partners span{font-size:17px;font-weight:700;color:#8c8c8c;display:flex;align-items:center;gap:7px}
.partners .badge{width:60px;height:64px;background:#cfcfcf;border-radius:50%}
.partners .sq{width:12px;height:12px;background:#999}

/* footer */
.footer{left:0;top:2156px;width:1200px;height:264px;background:#e4e4e4}
.fcol{position:absolute;top:30px;font-size:11.5px;line-height:21px}
.fcol h6{font-size:13.5px;font-weight:400;color:var(--blue-dark);margin-bottom:10px}
.fcol li{color:#777}
.fcol li.u{text-decoration:underline;color:var(--blue)}
.fcol li.d{color:#333}
.fcol.sep{border-left:1px solid #cfcfcf;padding-left:14px;height:200px}
.follow{position:absolute;left:886px;top:-12px;width:192px;height:276px;background:linear-gradient(#2e5b80,#224663);color:#fff;padding:22px 22px}
.follow h6{font-size:14px;font-weight:600;margin-bottom:10px}
.follow li{display:flex;align-items:center;gap:9px;font-size:12px;line-height:24px}
.follow li i{width:14px;height:12px;background:#e6eef5;border-radius:2px}
.follow li i.o{background:#e8892d}
.follow .join{margin-top:20px}
.bottombar{left:0;top:2420px;width:1200px;height:42px;background:var(--navy);color:#c9d6e2;font-size:11.5px;text-align:center;line-height:42px}
</style>
</head>
<body>

<div class="abs topbar">
  <div class="links"><span>Home</span><span class="on">About us</span><span>Take a tour</span><span>Advertise</span><span>Why Brindlework.net?</span><span class="like"><i></i>Like</span></div>
  <div class="acts"><span class="btn-light">Login</span><span class="btn-light">Sign Up</span><span class="btn-light">List Your Services</span></div>
</div>

<header class="abs header">
  <div class="logo"><i></i>Brindlework.net</div>
  <nav class="nav"><span>All trade services</span><span>Let us help you</span><span class="cur">Browse knowledge</span></nav>
</header>

<section class="abs hero">
  <div class="photo" role="img" aria-label="Businessman in a suit holding a tablet with an airplane rising from it"></div>
  <h1>Improve your business overseas!</h1>
  <p class="lead">Use the leverage of 51,000+ verified services providers:</p>
  <ul>
    <li>Sales agents, market entry, customs services</li>
    <li>Sourcing companies, freight forwarders, quality control</li>
    <li>Lawyers, accounting, expat services and more</li>
  </ul>
  <div class="search">
    <div class="field">Search 20,000+ content items &amp; 50,000+ services providers...</div>
    <div class="go"><svg width="18" height="18" viewBox="0 0 18 18"><circle cx="7.5" cy="7.5" r="5.5" fill="none" stroke="#fff" stroke-width="2"/><line x1="11.5" y1="11.5" x2="16" y2="16" stroke="#fff" stroke-width="2.4"/></svg></div>
  </div>
  <div class="listed">Includes the service providers listed by: <i></i></div>
</section>

<section class="abs start">
  <span class="label">Start now:</span>
  <div class="select">Select your target country <b><svg width="12" height="8"><path d="M1 1l5 5 5-5" fill="none" stroke="#666" stroke-width="2"/></svg></b></div>
  <span class="assist">and find assistance to</span>
  <span class="chk"><i></i>Import</span>
  <span class="chk on"><i>✕</i>Export</span>
  <span class="chk"><i></i>Invest</span>
  <span class="gobtn">GO</span>
</section>

<section class="abs country">
  <h2>Want to export to South Africa?<span>Discover 451 Service Providers to help you export including:</span></h2>
  <div class="arrows"><svg width="16" height="16"><path d="M8 2L2 8l6 6M14 2L8 8l6 6" fill="none" stroke="#999" stroke-width="2"/></svg><svg width="16" height="16"><path d="M2 2l6 6-6 6M8 2l6 6-6 6" fill="none" stroke="#999" stroke-width="2"/></svg></div>
  <div class="rule"></div>
  <div class="seal"></div>
  <div class="partner">
    <h3>Ardenvale South Africa</h3>
    <div class="sub">Export support</div>
    <p>Sed nibh sapien, elementum dignissim eleifend nec, adipiscing sit amet lectus. Donec quis tortor eros, ut egestas metus. Nunc posuere molestie ultrices.</p>
    <div class="foot"><a>www.ardenvale.com</a><span>Want your logo here?</span></div>
  </div>
  <div class="vline"></div>
  <div class="stat" style="left:518px"><div class="n">25</div><div class="t">Freight<br>Forwarders</div><div class="w">in South Africa</div><a>See all</a></div>
  <div class="stat" style="left:697px"><div class="n">47</div><div class="t">Corporate<br>Lawyers</div><div class="w">in South Africa</div><a>See all</a></div>
  <div class="stat" style="left:857px"><div class="n">56</div><div class="t">Debt<br>Collectors</div><div class="w">in South Africa</div><a>See all</a></div>
</section>

<section class="abs col dir">
  <h4>Browse our directory</h4>
  <div class="tabs"><span class="on">Services 200+</span><span>Countries 100+</span></div>
  <ul>
    <li>Freight Forwarders <em>(7843)</em></li>
    <li>Trading Companies <em>(2489)</em></li>
    <li>Coporate Law <em>(975)</em></li>
    <li class="sub">Investment Promotion (817)</li>
    <li>Distributors <em>(656)</em></li>
    <li>Tranlation <em>(621)</em></li>
    <li>Debt Collection <em>(561)</em></li>
    <li>Accounting Services <em>(519)</em></li>
    <li>Expat Services <em>(512)</em></li>
    <li>Market Research <em>(512)</em></li>
    <li>Debt Collection <em>(561)</em></li>
    <li>Freight Forwarders <em>(7843)</em></li>
    <li>Trading Companies <em>(2489)</em></li>
    <li>Coporate Law <em>(975)</em></li>
    <li>Investment Promotion <em>(817)</em></li>
    <li>Distributors <em>(656)</em></li>
    <li>Tranlation <em>(621)</em></li>
    <li>Debt Collection <em>(561)</em></li>
    <li>Accounting Services <em>(519)</em></li>
    <li>Expat Services <em>(512)</em></li>
    <li>Market Research <em>(512)</em></li>
    <li>Debt Collection <em>(561)</em></li>
    <li>Freight Forwarders <em>(7843)</em></li>
    <li>Trading Companies <em>(2489)</em></li>
    <li>Coporate Law <em>(975)</em></li>
    <li>Investment Promotion <em>(817)</em></li>
    <li>Distributors <em>(656)</em></li>
    <li>Tranlation <em>(621)</em></li>
    <li>Expat Services <em>(512)</em></li>
    <li>Market Research <em>(512)</em></li>
    <li>Debt Collection <em>(561)</em></li>
    <li>Freight Forwarders <em>(7843)</em></li>
    <li>Trading Companies <em>(2489)</em></li>
    <li>Coporate Law <em>(975)</em></li>
    <li>Investment Promotion <em>(817)</em></li>
    <li>Distributors <em>(656)</em></li>
    <li>Tranlation <em>(621)</em></li>
  </ul>
</section>

<section class="abs col say">
  <h4>What Importers / Exporters say</h4>
  <div class="quote">
    <div class="head"><div class="avatar" role="img" aria-label="Portrait of the speaker"></div><div><div class="nm">Name Of Speaker</div><div class="role">Sourcing Services</div><div class="loc">Florida, The United States</div></div></div>
    <span class="mark">“</span>
    <p>“Sed nibh sapien, elementum dignissim eleifend nec, adipiscing sit amet lectus. Donec quis tortor eros, ut egestas metus. Nunc posuere molestie ultrices. Morbi at dui id diam commodo venenatis eu in felis. Nam quis tellus non nibh lobortis placerat. Nam tristique metus in odio vehicula convallis. Donec condimentum elementum dui nec faucibus.”</p>
    <div class="bottom"><a>See the benefits</a></div>
  </div>
  <div class="quote">
    <div class="head"><div class="avatar" role="img" aria-label="Portrait of the speaker"></div><div><div class="nm">Name Of Speaker</div><div class="role">Investment Promotion</div><div class="loc">Dhaka, India</div></div></div>
    <span class="mark">“</span>
    <p>“Ut posuere porta aliquet. Fusce sollicitudin imperdiet odio, a semper est feugiat blandit. Morbi eros lorem, cursus non sollicitudin rutrum, sagittis et lacus.Nam eget purus arcu, id congue tortor. Donec facilisis purus quis libero malesuada vitae tempus elit condimentum.”</p>
    <div class="bottom"><a>See the benefits</a><span class="btn-white">Join for FREE</span></div>
  </div>
</section>

<section class="abs col tips">
  <h4>Business Tips By Experts</h4>
  <div class="tip"><h5>Business administration</h5><p>Nullam massa metus, eleifend nec tincidunt vel, scelerisque vel urna.</p><div class="rate"><span class="stars">★★★<b>★★</b></span>Rated <i class="pdf"></i></div></div>
  <div class="tip"><h5>Business administration</h5><p>Nullam massa metus, eleifend nec tincidunt vel, scelerisque vel urna.</p><div class="rate"><span class="stars">★★★<b>★★</b></span>Rated <i class="pdf"></i></div></div>
  <div class="tip"><h5>Business administration</h5><p>Nullam massa metus, eleifend nec tincidunt vel, scelerisque vel urna.</p><div class="rate"><span class="stars">★★★<b>★★</b></span>Rated <i class="pdf"></i></div></div>
  <div class="bottom"><span>Browse all content</span><span class="btn-white">Receive Updates</span></div>
</section>

<section class="abs col newsp">
  <h4>New Service Providers</h4>
  <div class="prov"><div class="lg"><i></i>Kestrel</div><div><h5>Kestrel Media Limited</h5><div class="cat">Tax Services in the United Kingdom</div><p>Lorem ipsum dolor sit amet, consectetur adipiscing elit. Suspendisse auctor quam sed magna ultricies rhoncus.</p><a>View Profile</a></div></div>
  <div class="prov"><div class="lg"><i></i>Harbourline</div><div><h5>Harbourline Trade Financing</h5><div class="cat">Factoring in the United States</div><p>Lorem ipsum dolor sit amet, quam a vestibulum dolor posuere non.</p><a>View Profile</a></div></div>
  <div class="prov" style="border:0"><div class="lg"><i></i>EMF</div><div><h5>Eastmere Materials Fed.</h5><div class="cat">Professional Association in China</div><p>Cum sociis natoque penatibus et magnis dis parturient montes, nascetur ridiculus mus.</p><a>View Profile</a></div></div>
  <div class="free">
    <div class="t">It's <b>FREE to list</b> your services on<br><span class="site">brindlework.net</span></div>
    <div class="b"><span>See the benefits</span><span class="btn-white">List Your Services</span></div>
  </div>
</section>

<section class="abs col know">
  <h4>Knowledge Resource</h4>
  <p class="intro">Find resources for your business amongst:</p>
  <ul>
    <li><b>10,145</b>Market analyses</li>
    <li><b>9,254</b>Business tips</li>
    <li><b>3,215</b>Agents and distributors</li>
    <li><b>50,145</b>Service providers</li>
  </ul>
  <div class="pick"><div class="select">Select a Country <b><svg width="12" height="8"><path d="M1 1l5 5 5-5" fill="none" stroke="#666" stroke-width="2"/></svg></b></div><span class="btn-blue">OK</span></div>
  <p class="pop">Most popular:</p>
  <p class="countries">China, Brazil, Japan, India, Egypt, Korea, Angola, Italy, England, Romania, <u>Spain</u>, Argentina, France, China, Brazil, Japan, India, Egypt, Korea, Angola, Africa, United States, Thailand, Singapore, Hungary, Germany, Russia, China, Vietnam, France</p>
</section>

<section class="abs partners">
  <span class="badge" role="img" aria-label="Partner badge"></span>
  <span>Norvane</span>
  <span>Tallwick</span>
  <span>Quillfen</span>
  <span>Marlowgate</span>
  <span><i class="sq"></i>Westbury Trade Office</span>
</section>

<footer class="abs footer">
  <div class="fcol" style="left:130px"><h6>About</h6><ul><li>About us</li><li>Partners</li><li>Site Map</li><li>Site Demo</li><li>Terms &amp; Conditions</li><li>Privacy Policy</li></ul></div>
  <div class="fcol sep" style="left:265px"><h6>Most Popular Pages</h6><ul><li>Distributors</li><li>Country Risk</li><li>Tax Law</li><li>Market Research</li><li>Business Development</li><li>Mergers and Acquisitions</li><li>Corporate Law</li><li class="d">View all</li></ul></div>
  <div class="fcol sep" style="left:455px"><h6>For Importers / Exporters</h6><ul><li>Import Export Services</li><li>Trade Companies, Agents</li><li>Market Analyses Worldwide</li><li class="u">International Business Tips</li><li>Receive Offers for Services</li><li class="d">Take a tour</li></ul></div>
  <div class="fcol sep" style="left:674px"><h6>For Service Providers</h6><ul><li>Import Export Services</li><li>Trade Companies, Agents</li><li>Market Analyses Worldwide</li><li>International Business Tips</li><li>Receive Offers for Services</li><li class="d" style="text-decoration:underline">Take a tour</li></ul></div>
  <div class="follow">
    <h6>Follow Us</h6>
    <ul><li><i></i>Newsletter</li><li><i></i>Chirpline</li><li><i class="o"></i>RSS</li></ul>
    <h6 class="join">Join Us</h6>
    <ul><li><i></i>Circlebook</li><li><i></i>Linkwell</li></ul>
  </div>
</footer>

<div class="abs bottombar">Brindlework.net - International Trade Resources, Import Export Services © 2012. All Rights Reserved.</div>

</body>
</html>
```